Letterhead Design for Vostrand Corporate Stationery

We are seeking a talented designer on ArtHive to create a professional and cohesive corporate stationery set for our company, Vostrand. Vostrand is a prominent player in the Commercial Real Estate industry, and we need stationery that reflects our brand's excellence and professionalism.

Scope of Work:

1. Letterhead Template (Microsoft Word):

Design a letterhead template in Microsoft Word format that adheres to our brand standards (attached in project files).
Include all necessary elements such as company logo, address, contact information, and any other relevant details.
The letterhead should be clean, elegant, and suitable for official business correspondence.

2. Business Cards:

Design business cards for our team members using the provided brand guidelines.
Include name, title, contact information, and the Vostrand logo.
Create a design that leaves a lasting impression and reflects our brand's professionalism.

3. Envelopes:

Design envelopes in various sizes (e.g., standard letter and legal sizes) that match the overall stationery theme.
Ensure that the design includes our company name, logo, and return address in accordance with brand guidelines.

4. Stationery:

Create a visually appealing stationery template that can be used for various documents and correspondence.
Ensure that the stationery design aligns with our brand standards and maintains consistency across all materials.

Submission Requirements:

Provide high-resolution files for each item (letterhead, business cards, envelopes, and stationery) in formats suitable for both print and digital use.
Include editable source files (e.g., Adobe Illustrator, Photoshop) for future modifications if necessary.

Design Guidelines:

Our brand is known for professionalism, trustworthiness, and excellence in the Commercial Real Estate industry. Please adhere to the brand standards provided in the project attachments.
Use our company colors, fonts, and logo as specified in the brand guidelines.
Feel free to be creative within the boundaries of our brand to make our stationery stand out while maintaining a professional look.

Budget and Timeline:

We are looking for high-quality designs at a competitive price.
The project timeline is flexible, but we would appreciate prompt responses from designers.
Please submit your best pricing and estimated delivery times with your proposals.
We look forward to receiving your creative and professional designs that will represent Vostrand in the best possible light. Thank you for considering our project, and we can't wait to see your submissions on ArtHive!

Target Market(s)

Our primary target market for the corporate stationery design project includes, but is not limited to: Investors: Individuals or entities interested in commercial real estate investment opportunities. Brokers: Commercial real estate brokers who facilitate property transactions and negotiations. Tenant Representatives: Professionals who advocate for the interests of tenants in commercial lease transactions. Lenders: Financial institutions and lenders involved in providing financing for commercial real estate projects. Property Owners: Owners of commercial real estate properties seeking professional correspondence materials. Industry Partners: Professionals and organizations within the commercial real estate industry who collaborate with or provide services to Vostrand. Prospective Clients: Potential clients or partners exploring opportunities in the commercial real estate sector. Please note that while these are the primary target market segments, the stationery design should also appeal to a broader audience within the commercial real estate industry and convey professionalism and trustworthiness to all stakeholders.

Industry/Entity Type

Commercial Real Estate

Font styles to use
Sans Serif

Colors
0054AA
0677BA
7BADD7
CADEEF
E8F1F8
0094D4
00A9DD
6FCCEA
C7EBF8
E9F6FB
F0912C
F2A743
F7CA91
FBE8D2
FDF5EE
EE7325
F08F49
F5BC92
FAE3D3
FDF4ED

Requirements
Must have
• Brand Consistency: Ensure that the design adheres to Vostrand's existing brand standards and guidelines (provided in project attachments). Professional Appearance: The stationery must convey professionalism, trustworthiness, and excellence in the Commercial Real Estate industry. Logo Usage: Integrate the Vostrand logo prominently and appropriately on all stationery items. Contact Information: Include accurate contact details, such as the company's address, phone number, email address, and website URL. Typography: Use the specified fonts from the brand guidelines for all text elements, maintaining consistency in font style and size. Color Palette: Utilize the designated brand colors consistently throughout the design. File Formats: Ensure that the final design files are provided in high-resolution formats suitable for both print and digital use. Also, request editable source files (e.g., Adobe Illustrator, Photoshop) for future modifications if needed. Print-Ready: Prepare the design files to be print-ready, including the appropriate bleed and margin specifications for printing purposes. Stationery Variations: Include designs for letterhead, business cards, envelopes (multiple sizes if applicable), and general stationery. Creativity within Brand Guidelines: Encourage designers to be creative while working within the boundaries of Vostrand's brand standards, making the stationery unique and eye-catching. Versatility: Ensure that the stationery can be easily adapted for various purposes, such as formal business correspondence, presentations, and more. Timely Delivery: Specify your preferred timeline for receiving initial design concepts and revisions. Budget: Indicate your budget range for the project to attract designers who can provide high-quality work within your financial constraints. Responsive Designers: Request that designers are responsive to messages and able to make necessary revisions in a timely manner.
Nice to have
• Creative Elements: Incorporate unique and creative design elements that align with Vostrand's brand identity and the Commercial Real Estate industry. Texture or Embossing: If applicable and within budget, consider incorporating textured or embossed elements to add a tactile dimension to the stationery. Custom Illustrations: Include custom illustrations or graphics that convey the essence of the commercial real estate industry or your company's mission and values. Watermark or Background Pattern: Consider adding a subtle watermark or background pattern that complements the overall design without distracting from the content. Custom Typography: Explore the use of custom typography or stylized lettering for headers or key text elements to make the stationery more visually appealing. Enhanced Print Options: If budget allows, opt for premium printing techniques like foil stamping, spot UV, or letterpress to make the stationery truly stand out. Digital Templates: Request digital templates for electronic documents, such as Microsoft Word templates, PowerPoint templates, or PDF templates, to maintain consistency in digital communications. Multiple Design Concepts: Ask for variations of the stationery design to choose from, providing you with options for different occasions or purposes. QR Codes: If relevant, consider incorporating QR codes that link to Vostrand's website, portfolio, or contact information for convenient access. Environmentally Friendly Options: Explore eco-friendly printing materials and practices to align with sustainability goals, if applicable. Mobile Optimization: Ensure that any digital templates or elements are optimized for mobile use, enhancing accessibility and usability. Social Media Icons: Include social media icons and links to Vostrand's social media profiles, if desired, for a comprehensive online presence. Alternate Color Schemes: Request variations of the design with alternate color schemes for seasonal or special occasions.
Should not have
• Non-Compliance with Brand Guidelines: Specify that the design must strictly adhere to Vostrand's brand guidelines, and any deviations are not acceptable. Excessive Complexity: Avoid overly complex designs that may clutter the stationery or distract from the essential information. Inconsistent Branding: Ensure that all design elements, including colors, fonts, and logo usage, remain consistent with the provided brand standards. Unapproved Fonts: Specify that designers should only use the approved fonts from the brand guidelines and avoid introducing new fonts. Inappropriate Imagery: Request that designers refrain from using images, illustrations, or graphics that are unrelated to the Commercial Real Estate industry or that could potentially be perceived as unprofessional. Overly Bright Colors: If it doesn't align with your brand, discourage the use of overly bright or neon colors that may not convey professionalism. Clashing Color Schemes: Ensure that the color scheme chosen for the design is harmonious and avoids color combinations that clash or are difficult to read. Overuse of Effects: Discourage excessive use of visual effects, such as gradients, drop shadows, or excessive transparency, which can make the stationery appear cluttered. Extravagant Printing Costs: Specify that designers should consider budget constraints and avoid design elements that would significantly increase printing costs, unless the budget allows for premium printing techniques. Outdated Design Trends: Request that the design avoids incorporating outdated design trends that may make the stationery appear dated. Inconsistent Branding Across Items: Ensure that the design maintains consistency across all stationery items (letterhead, business cards, envelopes, etc.) and that there are no significant variations that could create confusion. Overly Busy Layouts: Ask for designs that have a clean and professional appearance, avoiding overcrowded layouts that make it difficult to read or find essential information.

```html
<!DOCTYPE html>
<html lang="en">
<head>
<meta charset="utf-8">
<title>Vostrand Stationery Set</title>
<link rel="stylesheet" href="https://fonts.googleapis.com/css2?family=Montserrat:wght@400;600;700&family=Open+Sans:wght@400&display=swap">
<style>
  :root {
    --navy: #041e4c;
    --board: #a3a3a3;
    --paper: #ffffff;
    --ink: #1b1b1b;
    --muted: #7a7a7a;
    --wood: #f1e3a6;
  }
  * { margin: 0; padding: 0; box-sizing: border-box; }
  html, body { width: 1200px; height: 1200px; overflow: hidden; background: var(--paper); }
  body { font-family: "Montserrat", sans-serif; color: var(--navy); }
  .stage { position: relative; width: 1200px; height: 1200px; }
  .board { position: absolute; left: 1px; top: 107px; width: 1198px; height: 985px; background: var(--board); }
  .item { position: absolute; background: var(--paper); }

  .wordmark { font-family: "Montserrat", sans-serif; font-weight: 700; color: var(--navy);
    letter-spacing: 0.18em; white-space: nowrap; position: absolute; transform: translateX(-50%); line-height: 1; }

  .skyline { position: absolute; left: 0; right: 0; bottom: 0;
    background: linear-gradient(to bottom, #9aa6bd 0%, var(--navy) 70%); }

  /* bag */
  .bag { left: 62px; top: 264px; width: 358px; height: 500px; }
  .bag-handle { position: absolute; left: 145px; top: 186px; width: 196px; height: 170px;
    border: 10px solid var(--navy); border-bottom: none; border-radius: 98px 98px 0 0; }
  .bag .wordmark { left: 50%; top: 247px; font-size: 31px; }
  .bag .skyline { height: 31px; }

  /* letterhead */
  .letterhead { left: 471px; top: 263px; width: 386px; height: 494px; }
  .letterhead .wordmark { left: 50%; top: 56px; font-size: 11px; }
  .sender-name { position: absolute; left: 29px; top: 93px; font-size: 12.5px; font-weight: 600; }
  .sender-title { position: absolute; left: 29px; top: 110px; font-size: 7.5px; color: var(--muted); font-weight: 400; }
  .date-label { position: absolute; left: 228px; top: 117px; font-size: 9px; font-weight: 700; color: var(--ink); }
  .letter-body { position: absolute; left: 29px; top: 153px; width: 329px;
    font-family: "Open Sans", sans-serif; font-size: 7.2px; line-height: 8.1px; color: var(--ink);
    text-align: justify; letter-spacing: 0.04em; }
  .letter-body p + p { margin-top: 5px; }
  .signature-line { position: absolute; left: 29px; top: 402px; width: 69px; border-top: 1.5px solid var(--navy); }
  .signature-label { position: absolute; left: 45px; top: 408px; font-size: 7px; font-weight: 600; color: var(--ink); }
  .letterhead .company-block { left: 228px; top: 372px; }
  .letterhead .skyline { height: 36px; }

  .company-block { position: absolute; font-size: 7.5px; line-height: 11px; color: var(--muted); font-weight: 400; }
  .company-name { color: var(--navy); font-weight: 700; }
  .contact-list { list-style: none; }
  .contact-list li { display: flex; align-items: center; gap: 4px; }
  .icon { width: 6px; height: 6px; fill: var(--navy); flex: none; }

  /* pencil */
  .pencil { position: absolute; left: 996px; top: 294px; width: 17px; height: 345px; }
  .pencil-tip { position: absolute; left: 0; top: 0; }
  .pencil-body { position: absolute; left: 0; top: 23px; width: 17px; height: 322px;
    background: linear-gradient(to right, #fff 55%, #d9d9d9 100%); }
  .pencil-label { position: absolute; left: 3px; bottom: 18px; transform-origin: left bottom;
    transform: rotate(-90deg) translateY(100%); font-size: 6.5px; font-weight: 700; white-space: nowrap; line-height: 9px; }

  /* envelope */
  .envelope { left: 62px; top: 803px; width: 388px; height: 210px; background: transparent; }
  .envelope-flap { position: absolute; left: 0; top: 0; }
  .envelope .wordmark { left: 336px; top: 147px; font-size: 9px; }

  /* compliment slip */
  .slip { left: 471px; top: 828px; width: 399px; height: 173px; }
  .slip .wordmark { left: 50%; top: 50px; font-size: 9.5px; }
  .slip .contacts { left: 24px; top: 92px; }
  .slip .company-block.address { left: 250px; top: 98px; }
  .slip .skyline { height: 36px; }

  /* business cards */
  .card-front { left: 897px; top: 707px; width: 241px; height: 137px; }
  .card-front .wordmark { left: 50%; top: 65px; font-size: 15px; }
  .card-back { left: 897px; top: 864px; width: 241px; height: 137px; }
  .card-back .wordmark { left: 195px; top: 37px; font-size: 8px; }
  .card-name { position: absolute; left: 17px; top: 14px; font-size: 10px; font-weight: 600; }
  .card-title { position: absolute; left: 17px; top: 28px; font-size: 6px; color: var(--muted); font-weight: 400; }
  .card-back .company-block { left: 17px; top: 56px; font-size: 6px; line-height: 8.8px; }
  .card-back .icon { width: 5px; height: 5px; }
</style>
</head>
<body>
<svg width="0" height="0" style="position:absolute" aria-hidden="true">
  <defs>
    <symbol id="icon-phone" viewBox="0 0 10 10"><path d="M2 0.5 L3.8 2.6 L2.9 3.8 Q4 6 6.2 7.1 L7.4 6.2 L9.5 8 L8.3 9.5 Q1 8.5 0.5 1.7 Z"/></symbol>
    <symbol id="icon-mail" viewBox="0 0 10 10"><path d="M0 2 H10 V8 H0 Z" fill="currentColor"/><path d="M1 2.8 L5 5.6 L9 2.8" stroke="#fff" stroke-width="0.9" fill="none"/></symbol>
    <symbol id="icon-web" viewBox="0 0 10 10"><circle cx="5" cy="5" r="4.5"/><path d="M0.5 5 H9.5 M5 0.5 V9.5 M5 0.5 Q2.2 5 5 9.5 M5 0.5 Q7.8 5 5 9.5" stroke="#fff" stroke-width="0.7" fill="none"/></symbol>
    <symbol id="icon-social" viewBox="0 0 10 10"><rect x="1" y="1" width="8" height="8" rx="2" fill="none" stroke="currentColor" stroke-width="1.4"/></symbol>
  </defs>
</svg>

<main class="stage">
  <div class="board"></div>

  <!-- carrier bag -->
  <div class="bag-handle"></div>
  <section class="item bag">
    <span class="wordmark">VOSTRAND</span>
    <div class="skyline" role="img" aria-label="Skyline band of building silhouettes"></div>
  </section>

  <!-- letterhead -->
  <section class="item letterhead">
    <span class="wordmark">VOSTRAND</span>
    <h1 class="sender-name">Marcus Whitfield</h1>
    <p class="sender-title">Founder &amp; Director</p>
    <p class="date-label">Date:</p>
    <div class="letter-body">
      <p>Lorem Ipsum is simply dummy text of the printing and typesetting industry. Lorem Ipsum has been the industry's standard dummy text ever since the 1500s, when an unknown printer took a galley of type and scrambled it to make a type specimen book. It has survived not only five centuries, but also the leap into electronic typesetting, remaining essentially unchanged. It was popularised in the 1960s with the release of Typeset sheets containing Lorem Ipsum passages, and more recently with desktop publishing software like Pagewright including versions of Lorem Ipsum.</p>
      <p>It is a long established fact that a reader will be distracted by the readable content of a page when looking at its layout. The point of using Lorem Ipsum is that it has a more-or-less normal distribution of letters, as opposed to using 'Content here, content here', making it look like readable English. Many desktop publishing packages and web page editors now use Lorem Ipsum as their default model text, and a search for 'lorem ipsum' will uncover many web sites still in their infancy. Various versions have evolved over the years, sometimes by accident, sometimes on purpose (injected humour and the like).</p>
      <p>Contrary to popular belief, Lorem Ipsum is not simply random text. It has roots in a piece of classical Latin literature from 45 BC, making it over 2000 years old. Daniel Ashgrove, a Latin professor at Brookfield College, looked up one of the more obscure Latin words, consectetur, from a Lorem Ipsum passage, and going through the cites of the word in classical literature, discovered the undoubtable source. Lorem Ipsum comes from sections 1.10.32 and 1.10.33 of "de Ordine Rerum Civilium" (The Order of Civic Things) by Varrius, written in 45 BC. This book is a treatise on the theory of ethics, very popular during the Renaissance. The first line of Lorem Ipsum, "Lorem ipsum dolor sit amet..", comes from a line in section 1.10.32.</p>
    </div>
    <div class="signature-line"></div>
    <p class="signature-label">Signeture</p>
    <div class="company-block">
      <p class="company-name">Vostrand Commercial Real Estate</p>
      <p>4120 Harbor Crest Drive, Suite 300,<br>Fairmont, CA 90210</p>
      <ul class="contact-list" style="margin-top:2px">
        <li><svg class="icon"><use href="#icon-phone"/></svg>(555)-214-7730</li>
        <li><svg class="icon" style="color:var(--navy)"><use href="#icon-mail"/></svg>info@vostrandcre.com</li>
        <li><svg class="icon"><use href="#icon-web"/></svg>www.vostrand.com</li>
        <li><svg class="icon" style="color:var(--navy)"><use href="#icon-social"/></svg>Vostrand</li>
      </ul>
    </div>
    <div class="skyline" role="img" aria-label="Skyline band of building silhouettes"></div>
  </section>

  <!-- pencil -->
  <div class="pencil">
    <svg class="pencil-tip" width="17" height="24" viewBox="0 0 17 24" aria-hidden="true">
      <polygon points="8.5,0 17,23 0,23" fill="var(--wood)"/>
      <polygon points="8.5,0 11.3,8 5.7,8" fill="#000"/>
    </svg>
    <div class="pencil-body">
      <span class="pencil-label">Vostrand Commercial Real Estate</span>
    </div>
  </div>

  <!-- envelope -->
  <section class="item envelope">
    <svg class="envelope-flap" width="388" height="210" viewBox="0 0 388 210" aria-hidden="true">
      <path d="M0 0 H388 V210 H0 Z" fill="#fff"/>
      <path d="M0 20 Q0 0 20 0 H368 Q388 0 388 20 V32 L335 52 H53 L0 32 Z" fill="var(--navy)"/>
    </svg>
    <span class="wordmark">VOSTRAND</span>
  </section>

  <!-- compliment slip -->
  <section class="item slip">
    <span class="wordmark">VOSTRAND</span>
    <div class="company-block contacts">
      <ul class="contact-list">
        <li><svg class="icon"><use href="#icon-phone"/></svg>(555)-214-7730</li>
        <li><svg class="icon" style="color:var(--navy)"><use href="#icon-mail"/></svg>info@vostrandcre.com</li>
        <li><svg class="icon"><use href="#icon-web"/></svg>www.vostrand.com</li>
        <li><svg class="icon" style="color:var(--navy)"><use href="#icon-social"/></svg>Vostrand</li>
      </ul>
    </div>
    <div class="company-block address">
      <p class="company-name">Vostrand Commercial Real Estate</p>
      <p>4120 Harbor Crest Drive, Suite 300,<br>Fairmont, CA 90210</p>
    </div>
    <div class="skyline" role="img" aria-label="Skyline band of building silhouettes"></div>
  </section>

  <!-- business card, front -->
  <section class="item card-front">
    <span class="wordmark">VOSTRAND</span>
  </section>

  <!-- business card, back -->
  <section class="item card-back">
    <h2 class="card-name">Marcus Whitfield</h2>
    <p class="card-title">Founder &amp; Director</p>
    <span class="wordmark">VOSTRAND</span>
    <div class="company-block">
      <p class="company-name">Vostrand Commercial Real Estate</p>
      <p>4120 Harbor Crest Drive, Suite 300,<br>Fairmont, CA 90210</p>
      <ul class="contact-list" style="margin-top:3px">
        <li><svg class="icon"><use href="#icon-phone"/></svg>(555)-214-7730</li>
        <li><svg class="icon" style="color:var(--navy)"><use href="#icon-mail"/></svg>info@vostrandcre.com</li>
        <li><svg class="icon"><use href="#icon-web"/></svg>www.vostrand.com</li>
        <li><svg class="icon" style="color:var(--navy)"><use href="#icon-social"/></svg>@Vostrand</li>
      </ul>
    </div>
  </section>
</main>
</body>
</html>
```